KLMR stationery 2023

Our stationery dates back to 2007 when we changed practice rooms.
We would like to have kept the logo and spiced up the design, especially since we have one more colleague (Dr. Henriette Bollmeyer)
Our practice colors are a slightly more muted pink and sand-colored.
Follow-up orders for flyers, notices, etc. are still waiting for this design.

```html
<!DOCTYPE html>
<html lang="de">
<head>
<meta charset="utf-8">
<title>KLMR Briefpapier</title>
<link rel="stylesheet" href="https://fonts.googleapis.com/css2?family=Encode+Sans+Condensed:wght@400;500;700&display=swap">
<style>
  :root {
    --backdrop: #2e1729;
    --paper: #ffffff;
    --pink: #b95fa5;
    --pink-faint: #f4e8f1;
    --sand: #e3c27e;
    --ink: #222222;
  }
  * { margin: 0; padding: 0; box-sizing: border-box; }
  html, body {
    width: 1200px; height: 1200px; overflow: hidden;
    background: var(--backdrop);
    font-family: "Encode Sans Condensed", "Arial Narrow", sans-serif;
    color: var(--ink);
  }
  .letterhead {
    position: absolute; left: 203px; top: 48px;
    width: 797px; height: 1118px;
    background: var(--paper);
    overflow: hidden;
  }
  .brand {
    position: absolute; top: 18px; left: 0; width: 100%;
    display: flex; justify-content: center; align-items: center; gap: 12px;
  }
  .brand-dot { width: 14px; height: 14px; border-radius: 50%; background: var(--pink); }
  .brand-name {
    font-size: 58px; font-weight: 400; letter-spacing: 4px; line-height: 1;
    color: var(--ink);
  }
  .team {
    position: absolute; top: 91px; left: 35px; right: 36px;
    display: flex; justify-content: space-between;
    list-style: none; font-size: 14.5px; font-weight: 500;
  }
  .team li { display: flex; align-items: center; gap: 7px; }
  .team li::before {
    content: ""; width: 5px; height: 5px; border-radius: 50%; background: var(--pink);
  }
  .decor {
    position: absolute; left: 14px; top: 856px; width: 218px; height: 248px;
    background: linear-gradient(180deg, rgba(244,232,241,0.4), var(--pink-faint));
    border-radius: 90px 90px 0 0;
  }
  .footer { position: absolute; left: 250px; width: 524px; top: 977px; }
  .rule-sand { height: 1px; background: var(--sand); }
  .rule-pink { height: 1px; background: var(--pink); position: absolute; top: 54px; left: 0; right: 0; }
  .services { position: absolute; top: 7px; left: 0; width: 100%; font-size: 12.6px; }
  .services li { position: absolute; list-style: none; display: flex; align-items: center; gap: 6px; white-space: nowrap; }
  .tick { width: 14px; height: 14px; flex: none; }
  .contact { position: absolute; top: 62px; left: 0; width: 100%; font-size: 12px; line-height: 18px; }
  .contact-col { position: absolute; display: flex; gap: 6px; }
  .icon { width: 14px; height: 14px; flex: none; margin-top: 2px; }
  .hours { position: absolute; top: 102px; left: 1px; font-size: 12px; white-space: nowrap; }
  .hours .label { color: var(--pink); margin-right: 5px; }
  .hours b { font-weight: 700; }
  .band { position: absolute; left: 0; right: 0; bottom: 0; height: 14px; background: var(--pink); }
</style>
</head>
<body>
<main class="letterhead">
  <header class="brand">
    <span class="brand-dot"></span>
    <span class="brand-name">KLMR</span>
  </header>

  <ul class="team">
    <li>Dr. Margrit Hallwyler</li>
    <li>Dr. Sabine Telloni</li>
    <li>Dr. Lukas Hallwyler</li>
    <li>Dr. Ildikó Varannai</li>
    <li>Dr. Henriette Bollmeyer</li>
  </ul>

  <div class="decor" role="img" aria-label="Faint silhouette illustration of a mother, a pregnant woman and a girl"></div>

  <footer class="footer">
    <div class="rule-sand"></div>
    <ul class="services">
      <li style="left:0;top:0"><svg class="tick" viewBox="0 0 14 14"><circle cx="7" cy="7" r="7" fill="#b95fa5"/><path d="M3.8 7.2l2.2 2.2 4.2-4.4" stroke="#fff" stroke-width="1.8" fill="none" stroke-linecap="round" stroke-linejoin="round"/></svg>Fachärzte für Gynäkologie und Geburtshilfe</li>
      <li style="left:230px;top:0"><svg class="tick" viewBox="0 0 14 14"><circle cx="7" cy="7" r="7" fill="#b95fa5"/><path d="M3.8 7.2l2.2 2.2 4.2-4.4" stroke="#fff" stroke-width="1.8" fill="none" stroke-linecap="round" stroke-linejoin="round"/></svg>Pränataldiagnostik</li>
      <li style="left:377px;top:0"><svg class="tick" viewBox="0 0 14 14"><circle cx="7" cy="7" r="7" fill="#b95fa5"/><path d="M3.8 7.2l2.2 2.2 4.2-4.4" stroke="#fff" stroke-width="1.8" fill="none" stroke-linecap="round" stroke-linejoin="round"/></svg>Schwangerschaftsbetreuung</li>
      <li style="left:0;top:22px"><svg class="tick" viewBox="0 0 14 14"><circle cx="7" cy="7" r="7" fill="#b95fa5"/><path d="M3.8 7.2l2.2 2.2 4.2-4.4" stroke="#fff" stroke-width="1.8" fill="none" stroke-linecap="round" stroke-linejoin="round"/></svg>Kinderwunschbehandlung</li>
      <li style="left:230px;top:22px"><svg class="tick" viewBox="0 0 14 14"><circle cx="7" cy="7" r="7" fill="#b95fa5"/><path d="M3.8 7.2l2.2 2.2 4.2-4.4" stroke="#fff" stroke-width="1.8" fill="none" stroke-linecap="round" stroke-linejoin="round"/></svg>Ambulante Operationen</li>
      <li style="left:377px;top:22px"><svg class="tick" viewBox="0 0 14 14"><circle cx="7" cy="7" r="7" fill="#b95fa5"/><path d="M3.8 7.2l2.2 2.2 4.2-4.4" stroke="#fff" stroke-width="1.8" fill="none" stroke-linecap="round" stroke-linejoin="round"/></svg>Onkologische Betreuung</li>
    </ul>
    <div class="rule-pink"></div>

    <div class="contact">
      <div class="contact-col" style="left:0">
        <svg class="icon" viewBox="0 0 14 14"><circle cx="7" cy="7" r="6.4" fill="none" stroke="#b95fa5" stroke-width="0.9"/><circle cx="7" cy="5.8" r="1.6" fill="none" stroke="#b95fa5" stroke-width="0.9"/><path d="M7 10.5L5 7.2M7 10.5L9 7.2" stroke="#b95fa5" stroke-width="0.9"/></svg>
        <address style="font-style:normal">Ahornweg 14<br>8400 Seewilen</address>
      </div>
      <div class="contact-col" style="left:188px">
        <div style="display:flex;flex-direction:column;gap:4px">
          <svg class="icon" viewBox="0 0 14 14"><circle cx="7" cy="7" r="6.4" fill="none" stroke="#b95fa5" stroke-width="0.9"/><path d="M4.5 4.2c0 3 2.3 5.4 5.3 5.4l.6-1.3-1.5-.8-.7.8c-1-.4-1.8-1.2-2.2-2.2l.8-.7-.8-1.5z" fill="#b95fa5"/></svg>
          <svg class="icon" viewBox="0 0 14 14"><circle cx="7" cy="7" r="6.4" fill="none" stroke="#b95fa5" stroke-width="0.9"/><rect x="4.3" y="5.5" width="5.4" height="4.2" fill="none" stroke="#b95fa5" stroke-width="0.9"/><rect x="5.3" y="3.8" width="3.4" height="1.7" fill="#b95fa5"/></svg>
        </div>
        <div>052 / 481 16 20<br>052 / 481 16 22</div>
      </div>
      <div class="contact-col" style="left:373px">
        <div style="display:flex;flex-direction:column;gap:4px">
          <svg class="icon" viewBox="0 0 14 14"><circle cx="7" cy="7" r="6.4" fill="none" stroke="#b95fa5" stroke-width="0.9"/><rect x="4" y="5" width="6" height="4.2" fill="none" stroke="#b95fa5" stroke-width="0.8"/><path d="M4 5l3 2.4L10 5" fill="none" stroke="#b95fa5" stroke-width="0.8"/></svg>
          <svg class="icon" viewBox="0 0 14 14"><circle cx="7" cy="7" r="6.4" fill="none" stroke="#b95fa5" stroke-width="0.9"/><circle cx="7" cy="7" r="3.4" fill="none" stroke="#b95fa5" stroke-width="0.8"/><path d="M3.6 7h6.8M7 3.6v6.8" stroke="#b95fa5" stroke-width="0.7"/></svg>
        </div>
        <div>praxis@klmr-seewilen.ch<br>www.klmr-seewilen.ch</div>
      </div>
    </div>

    <p class="hours"><span class="label">Öffnungszeiten:</span>Montag - Freitag <b>08.00 - 12.00 Uhr</b> und <b>13.00 - 17.30 Uhr</b></p>
  </footer>

  <div class="band"></div>
</main>
</body>
</html>
```